New design for a hotel booking website

I am looking to re-design my hotel booking website peakstaylodging.net. Please find the specs attached. Delivery in PSD format. Two pages total: (i) homepage and (ii) inner page.
I want the design to be very simple to navigate and have a feel that is related to Banff, Canada. You can keep a similar layout as the current website.
Requirements
1) Homepage
- Booking form above the fold containing the check in & check out dates, # of rooms and the Search button
- Quality image relating to the city of Banff to make it clear what city this is (no slider - I don't want any animation)
- A section for featured hotels (3-5 items)
- A section for links to other sections on the website (currently under "Explore Banff")
- A section for articles and local guides
- A weather widget (either in the header or somewhere else, similar to this one http://clipvanta.com/t/QX7RLPd2K4)
2) Hotel listings page - http://www.peakstaylodging.net/hotels
- Left or right sidebar – must contain the booking form with the same fields as on the homepage
- A section of why to book hotels with us under the booking form
- Each hotel listing should contain the following
Hotel name
Star rating
Short description (same as currently on the website)
Thumbnail
Address
A button to Check Rates
Notes
- I want the design to be user friendly, simple and easy to use
- I want it to be related to Banff. Banff is a resort town in Alberta, Canada with mountains for skiing in the winter and parks and wildlife nature in the summer.
- Delivery format: PSD
- I want the layout to be easily convertible into a responsive design
- Small social media icon to the Chatterly page (with the option to add Vidzo and Quippr in the future)
Some competing website examples:
1) corvelridgeway.com/Places-to-Stay/Hotels-Inns
2) tornivastays.org
Some examples of websites I liked:
1) http://www.quellmont.com/accommodation/hotels/
2) http://www.lodgevanterra.com/
Target Market(s)
Anyone looking to book their stay in Banff, AB, Canada.
Industry/Entity Type
Travel
Number of Pages Required
2 page
Look and feel

```html
<!DOCTYPE html>
<html lang="en">
<head>
<meta charset="utf-8">
<title>PeakStay Lodging – Compare Prices on Accommodations in Banff</title>
<link rel="stylesheet" href="https://fonts.googleapis.com/css2?family=Lato:ital,wght@0,300;0,400;0,700;0,900;1,700&family=Tinos&display=swap">
<style>
:root{
  --orange:#f89a0c;
  --orange-dark:#e58600;
  --blue:#1f9ad9;
  --blue-dark:#137fc0;
  --slate:#4a5863;
  --ink:#1d1d1d;
  --text:#444;
  --muted:#888;
  --line:#dcdcdc;
  --pale:#e8f4f5;
  --bar:#1a1a1a;
  --white:#fff;
}
*{box-sizing:border-box;margin:0;padding:0}
html,body{width:1200px;height:2740px;overflow:hidden}
body{position:relative;font-family:'Lato',sans-serif;color:var(--text);background:var(--white)}
.abs{position:absolute}

/* Header */
.site-header{position:absolute;left:0;top:0;width:1200px;height:130px;background:var(--white)}
.brand{position:absolute;left:128px;top:44px}
.brand-name{font:900 29px/1 'Lato',sans-serif;color:var(--blue-dark);letter-spacing:-.3px}
.brand-tag{margin-top:6px;font:700 10.5px/1 'Lato',sans-serif;color:var(--blue);letter-spacing:.3px}
.lang{position:absolute;left:1005px;top:32px;font-size:10px;color:var(--ink);display:flex;align-items:center;gap:6px}
.lang .flag{width:14px;height:9px;background:linear-gradient(#b22234 0 33%,#fff 33% 66%,#b22234 66%)}
.lang .caret{margin-left:20px;font-size:9px}
.season{position:absolute;left:745px;top:60px;width:153px;height:28px;background:#1b1b1b;display:flex;align-items:center;justify-content:center;gap:6px;font:700 10px 'Lato',sans-serif;color:var(--white)}
.season .summer{color:var(--orange)}
.search-box{position:absolute;left:898px;top:60px;width:170px;height:28px;background:#e9e9e9;display:flex}
.search-box span{flex:1;padding:0 8px;font-size:9px;color:#aaa;line-height:28px}
.search-box i{width:26px;background:#7c7c7c;display:flex;align-items:center;justify-content:center}

/* Nav */
.main-nav{position:absolute;left:0;top:130px;width:1200px;height:46px;background:linear-gradient(#2aa7e6,#1688cc)}
.main-nav ul{list-style:none;position:absolute;left:130px;top:0;display:flex;height:46px}
.main-nav li{font:400 13px/46px 'Lato',sans-serif;color:var(--white);padding:0 21px}
.main-nav li.active{background:#555d63}

/* Hero */
.hero{position:absolute;left:0;top:176px;width:1200px;height:514px}
.hero-photo{position:absolute;inset:0;background:linear-gradient(180deg,#bcd9ec 0%,#e4eef3 35%,#b7d6d6 60%,#c8ddd9 100%)}
.hero-title{position:absolute;left:128px;top:141px;font:300 34px/44px 'Lato',sans-serif;color:var(--ink)}
.hero-title b{font-weight:900}
.btn-book{position:absolute;left:128px;top:306px;width:162px;height:38px;border-radius:19px;background:linear-gradient(#fcae2c,var(--orange-dark));color:var(--white);font:700 14px/38px 'Lato',sans-serif;text-align:center}
.hero-note{position:absolute;left:300px;top:318px;font-size:11px;color:var(--ink)}

/* Booking panel */
.booking{position:absolute;left:842px;top:130px;width:248px;height:447px;background:var(--slate)}
.booking-head{height:60px;background:var(--orange);color:var(--white);font:700 16px/60px 'Lato',sans-serif;text-align:center;letter-spacing:.2px}
.field{padding:0 12px}
.field label{display:block;font-size:11px;line-height:13px;color:var(--white);margin:12px 0 5px}
.field:first-of-type label{margin-top:16px}
.select{height:30px;background:var(--white);border:1px solid #ccc;display:flex;align-items:center;justify-content:space-between;font-size:10px;color:var(--ink);padding-left:8px}
.select i{width:22px;height:28px;background:#dcdcdc;display:flex;align-items:center;justify-content:center;font-style:normal;font-size:9px}
.btn-submit{margin:18px 12px 0;height:36px;border-radius:18px;background:linear-gradient(#fcae2c,var(--orange-dark));color:var(--white);font:700 13px/36px 'Lato',sans-serif;text-align:center}

/* Section headings */
.section-title{position:absolute;left:0;width:1200px;text-align:center;font:400 28px/1 'Tinos',serif;color:var(--ink);letter-spacing:.5px}
.section-lead{position:absolute;left:265px;width:670px;text-align:center;font-size:11.5px;line-height:19px;color:var(--ink)}

/* Featured */
.hotel-card{position:absolute;top:853px;width:302px;height:397px;border:1px solid var(--line);background:var(--white)}
.hotel-photo{height:206px}
.hotel-card h3{margin:17px 7px 0;font:400 17px/20px 'Lato',sans-serif;color:var(--ink)}
.hotel-card p{margin:6px 7px 0;font-size:11px;line-height:24px;color:var(--muted)}
.hotel-price{position:absolute;left:7px;bottom:14px;font-size:10px;color:#666}
.hotel-price strong{display:block;font-weight:400;font-size:16px;color:var(--ink);margin-top:2px}
.btn-view{position:absolute;right:19px;bottom:16px;width:88px;height:28px;background:var(--orange);color:var(--white);font-size:11px;line-height:28px;text-align:center}

/* Explore */
.explore{position:absolute;left:0;top:1298px;width:1200px;height:740px;background:var(--pale)}
.tile{position:absolute;width:315px;height:262px}
.tile-cap{position:absolute;left:0;right:0;bottom:0;height:64px;background:rgba(20,20,20,.6);color:var(--white);padding:13px 14px 0}
.tile-cap .kicker{font:italic 700 11px 'Lato',sans-serif}
.tile-cap .name{font:700 14px 'Lato',sans-serif;margin-top:4px}
.tile-cap .days{position:absolute;right:16px;top:13px;font:700 11px 'Lato',sans-serif;text-align:right}
.tile-cap .days span{display:block;font-size:18px;font-weight:400;margin-top:3px}

/* CTA */
.signup{position:absolute;left:0;top:2038px;width:1200px;height:348px;background:linear-gradient(180deg,#1d2f3d,#26394a 60%,#1e2e3b)}
.signup h2{position:absolute;left:0;width:1200px;top:68px;text-align:center;font:700 34px 'Lato',sans-serif;color:var(--white)}
.signup p{position:absolute;left:0;width:1200px;top:118px;text-align:center;font:700 16px 'Lato',sans-serif;color:var(--white)}
.input{position:absolute;top:2208px;height:42px;width:325px;background:var(--white);font-size:12px;color:#777;line-height:42px;padding-left:16px}
.btn-start{position:absolute;left:237px;top:2268px;width:658px;height:48px;background:var(--orange);color:var(--white);font:700 20px/48px 'Lato',sans-serif;text-align:center}

/* Footer */
.site-footer{position:absolute;left:0;top:2386px;width:1200px;height:314px;background:var(--white)}
.foot-h{position:absolute;top:52px;font:400 17px 'Lato',sans-serif;color:var(--ink)}
.foot-list{position:absolute;top:92px;list-style:none}
.foot-list li{font-size:11px;color:#777;line-height:29px;padding-left:16px;position:relative}
.foot-list li::before{content:"";position:absolute;left:0;top:12px;border-left:5px solid #aaa;border-top:3px solid transparent;border-bottom:3px solid transparent}
.news{position:absolute;left:380px;width:200px;height:90px}
.news .thumb{position:absolute;left:0;top:0;width:54px;height:51px;background:linear-gradient(135deg,#6fb6d8,#e4b36a)}
.news h4{margin:4px 0 0 64px;font:400 12px 'Lato',sans-serif;color:var(--orange)}
.news p{margin:14px 0 0 64px;font-size:9px;color:#777}
.news time{display:block;margin:20px 0 0 64px;font-size:9px;color:#777}
.foot-text{position:absolute;font-size:10px;line-height:17px;color:#888}
.mail{position:absolute;left:625px;top:145px;width:228px;height:31px;background:#efefef;font-size:10px;color:#777;line-height:31px;padding-left:14px}
.mail i{position:absolute;right:0;top:0;width:28px;height:31px;background:var(--orange);display:flex;align-items:center;justify-content:center}
.help{position:absolute;left:877px;top:155px}
.help h5{font:400 15px 'Lato',sans-serif;color:var(--ink);margin-left:30px}
.help a{display:block;font-size:13px;color:var(--orange);margin:5px 0 0 30px;text-decoration:none}
.socials{position:absolute;left:877px;top:230px;display:flex;gap:3px}
.socials span{width:26px;height:26px;background:#c8cfd4}
.copy{position:absolute;left:0;top:2700px;width:1200px;height:40px;background:var(--bar);color:#ddd;font-size:12px;line-height:40px;text-align:center}
</style>
</head>
<body>

<header class="site-header">
  <div class="brand">
    <div class="brand-name">PEAKSTAY LODGING</div>
    <div class="brand-tag">COMPARE PRICES ON ACCOMMODATIONS IN BANFF</div>
  </div>
  <div class="lang"><span class="flag"></span>ENG<span class="caret">▼</span></div>
  <div class="season"><span class="summer">☀ SUMMER</span><span>❄ WINTER</span></div>
  <div class="search-box"><span>Search</span><i><svg width="13" height="13" viewBox="0 0 13 13"><circle cx="5.5" cy="5.5" r="4" fill="none" stroke="#fff" stroke-width="1.8"/><line x1="8.5" y1="8.5" x2="12" y2="12" stroke="#fff" stroke-width="2"/></svg></i></div>
</header>

<nav class="main-nav">
  <ul>
    <li class="active">Home</li><li>Banff Hotels</li><li>Banff Resort</li><li>Lodges</li><li>Inns &amp; Motels</li><li>FAQs</li><li>Contact Us</li>
  </ul>
</nav>

<section class="hero">
  <div class="hero-photo" role="img" aria-label="Traveller with a camera wading in clear turquoise water in front of waterfront holiday villas under a bright sky"></div>
  <h1 class="hero-title"><b>Best</b> You Choose<br>Choose From <b>Over 47</b><br><b>Hotels</b> Resort and inss</h1>
  <div class="btn-book">BOOK NOW</div>
  <div class="hero-note">All of our Services are FREE</div>
</section>

<aside class="booking">
  <div class="booking-head">SEARCH BANFF HOTELS</div>
  <div class="field"><label>Check in</label><div class="select">Immediately<i>▼</i></div></div>
  <div class="field"><label>Check Out</label><div class="select">Immediately<i>▼</i></div></div>
  <div class="field"><label>Rooms</label><div class="select">1<i>▼</i></div></div>
  <div class="field"><label>Adults</label><div class="select">Age<i>▼</i></div></div>
  <div class="field"><label>Children</label><div class="select">0<i>▼</i></div></div>
  <div class="btn-submit">SUBMIT HERE</div>
</aside>

<h2 class="section-title" style="top:735px">FEATURED HOTEL</h2>
<p class="section-lead" style="top:776px">Lorem Ipsum is simply dummy text of the printing and typesetting industry. Lorem Ipsum has been the industry's standard<br>dummy text ...ever since the 1500s, when an unknown printer took a galley..</p>

<article class="hotel-card" style="left:128px">
  <div class="hotel-photo" role="img" aria-label="City skyline with a tall tower reflected on the lake at dusk" style="background:linear-gradient(180deg,#7fa9d4,#c99bb0 55%,#3d4c6a)"></div>
  <h3>Lorem Ipsum</h3>
  <p>Lorem Ipsum is simply dummy text of the print-<br>ing and typesetting industry. Lorem Ipsum has<br>been the industry's standard dummy text ...</p>
  <div class="hotel-price">STARTS FROM<strong>&amp;0.00</strong></div>
  <div class="btn-view">View Details</div>
</article>
<article class="hotel-card" style="left:444px">
  <div class="hotel-photo" role="img" aria-label="Mountain lake hotel framed by snowy peaks and pine forest" style="background:linear-gradient(180deg,#5f8fc4,#a9c1d4 40%,#4e6a4a 75%,#2f4530)"></div>
  <h3>Lorem Ipsum</h3>
  <p>Lorem Ipsum is simply dummy text of the print-<br>ing and typesetting industry. Lorem Ipsum has<br>been the industry's standard dummy text ...</p>
  <div class="hotel-price">STARTS FROM<strong>&amp;0.00</strong></div>
  <div class="btn-view">View Details</div>
</article>
<article class="hotel-card" style="left:769px">
  <div class="hotel-photo" role="img" aria-label="Colourful alpine village houses beside a stream with a cable car above" style="background:linear-gradient(180deg,#6d9bd1,#b6a99a 45%,#6f7f4a 80%,#4a5a3a)"></div>
  <h3>Lorem Ipsum</h3>
  <p>Lorem Ipsum is simply dummy text of the print-<br>ing and typesetting industry. Lorem Ipsum has<br>been the industry's standard dummy text ...</p>
  <div class="hotel-price">STARTS FROM<strong>&amp;0.00</strong></div>
  <div class="btn-view">View Details</div>
</article>

<section class="explore">
  <h2 class="section-title" style="top:42px">EXPLORE BENFITS</h2>
  <p class="section-lead" style="top:83px">Lorem Ipsum is simply dummy text of the printing and typesetting industry. Lorem Ipsum has been the industry's standard<br>dummy text ...ever since the 1500s, when an unknown printer took a galley..</p>

  <div class="tile" style="left:131px;top:150px" role="img" aria-label="Couple in sun hats looking over a tropical bay">
    <div style="position:absolute;inset:0;background:linear-gradient(160deg,#4f9ad6,#7fc6c0 55%,#c7b28a)"></div>
    <div class="tile-cap"><div class="kicker">LOREM</div><div class="name">Ipsum Dolar Sit</div><div class="days">2 DAYS<span>&amp;0.00</span></div></div>
  </div>
  <div class="tile" style="left:447px;top:150px" role="img" aria-label="Family waving on a sandy beach">
    <div style="position:absolute;inset:0;background:linear-gradient(170deg,#3f8fd2,#9fc8e4 45%,#d9b98e)"></div>
    <div class="tile-cap"><div class="kicker">LOREM</div><div class="name">Ipsum Dolar Sit</div><div class="days">2 DAYS<span>&amp;0.00</span></div></div>
  </div>
  <div class="tile" style="left:763px;top:150px;width:303px" role="img" aria-label="Two people relaxing in deck chairs facing a turquoise sea">
    <div style="position:absolute;inset:0;background:linear-gradient(170deg,#2f7fc9,#7ec2e3 45%,#3aa7b3 70%,#b5793f)"></div>
    <div class="tile-cap"><div class="kicker">LOREM</div><div class="name">Ipsum Dolar Sit</div><div class="days">2 DAYS<span>&amp;0.00</span></div></div>
  </div>
  <div class="tile" style="left:131px;top:412px;height:264px" role="img" aria-label="Group of friends jumping on the beach">
    <div style="position:absolute;inset:0;background:linear-gradient(170deg,#4aa1e0,#a9d5ee 50%,#d7c7a2)"></div>
    <div class="tile-cap"><div class="kicker">LOREM</div><div class="name">Ipsum Dolar Sit</div><div class="days">2 DAYS<span>&amp;0.00</span></div></div>
  </div>
  <div class="tile" style="left:447px;top:412px;height:264px" role="img" aria-label="Couple taking a selfie among tropical greenery">
    <div style="position:absolute;inset:0;background:linear-gradient(160deg,#3f7d3a,#8fae5a 45%,#c99a6e)"></div>
    <div class="tile-cap"><div class="kicker">LOREM</div><div class="name">Ipsum Dolar Sit</div><div class="days">2 DAYS<span>&amp;0.00</span></div></div>
  </div>
  <div class="tile" style="left:763px;top:412px;width:303px;height:264px" role="img" aria-label="Lifeguard hut on the beach at sunset">
    <div style="position:absolute;inset:0;background:linear-gradient(180deg,#3d6fa8,#e9a54a 50%,#c9723a 75%,#5a4a3a)"></div>
    <div class="tile-cap"><div class="kicker">LOREM</div><div class="name">Ipsum Dolar Sit</div><div class="days">2 DAYS<span>&amp;0.00</span></div></div>
  </div>
</section>

<section class="signup" role="img" aria-label="Dimmed photo of friends relaxing on beach cushions behind the signup form">
  <h2>Plan Better Do More Enjoy Your Break</h2>
  <p>Why Should anyone sign uo to you email list? Let them Know here.</p>
</section>
<div class="input" style="left:237px">Name</div>
<div class="input" style="left:570px">Email</div>
<div class="btn-start">GET STARTED</div>

<footer class="site-footer">
  <h3 class="foot-h" style="left:134px">About</h3>
  <ul class="foot-list" style="left:128px">
    <li>Safety</li><li>Roamly Pics</li><li>Mobile</li><li>Why Host</li><li>Social Connect</li><li>Site Map</li>
  </ul>
  <ul class="foot-list" style="left:252px;top:90px">
    <li>About</li><li>Lates Job</li><li>Press Release</li><li>Blog Posts</li><li>Help Topics</li><li>Polices</li>
  </ul>

  <h3 class="foot-h" style="left:380px">Latest News</h3>
  <div class="news" style="top:88px">
    <div class="thumb" role="img" aria-label="Small travel photo"></div>
    <h4>Beautifull Placess</h4>
    <p>Lorem Ipsum is simply dummy</p>
    <time>January 15,2015</time>
  </div>
  <div class="news" style="top:199px">
    <div class="thumb" role="img" aria-label="Small travel photo"></div>
    <h4>Travel With Security</h4>
    <p>Lorem Ipsum is simply dummy</p>
    <time>January 15,2015</time>
  </div>

  <h3 class="foot-h" style="left:625px">Mailing List</h3>
  <p class="foot-text" style="left:625px;top:90px;width:230px">Sign up for our mailing listto get latest updates and offers..</p>
  <div class="mail">your email<i><svg width="12" height="10" viewBox="0 0 12 10"><path d="M1 5l3.5 3.5L11 1" fill="none" stroke="#fff" stroke-width="2"/></svg></i></div>
  <p class="foot-text" style="left:625px;top:192px">We respect our privacy</p>

  <h3 class="foot-h" style="left:877px">Nees Roamly Help?</h3>
  <p class="foot-text" style="left:877px;top:90px;width:215px">We would more than happy to help you team advisor are 24/7 at your service to help you.</p>
  <div class="help">
    <svg class="abs" style="left:0;top:2px" width="18" height="18" viewBox="0 0 24 24"><path d="M6.6 10.8a15 15 0 006.6 6.6l2.2-2.2a1 1 0 011-.25 11.4 11.4 0 003.6.6 1 1 0 011 1V20a1 1 0 01-1 1A17 17 0 013 4a1 1 0 011-1h3.5a1 1 0 011 1c0 1.25.2 2.45.6 3.6a1 1 0 01-.25 1z" fill="#f89a0c"/></svg>
    <h5>Nees Roamly Help?</h5>
    <a>hello@roamlyisle.com</a>
  </div>
  <div class="socials"><span></span><span></span><span></span><span></span><span></span><span></span><span></span></div>
</footer>
<div class="copy">Copyright © 2015 - PeakStay Lodging - All Rights Reserved</div>

</body>
</html>
```